PowerPoint Design Project

Lanterfield Estate Partners is a Melbourne based property development management company. We provide a comprehensive range of development management services to a select group of listed developers, private landowners, overseas investors and development partners and institutional clients. Our website provides additional information about the company:
http://www.lanterfieldep.example.au
We are looking for a versatile powerpoint design that can be used across a wide variety of presentations including; pitch documents, client reports, Information memorandums, and downloadable credential packs etc. We have attached a good example document.
Updates

Industry/Entity Type

It Company

Requirements
Must have
• The design should have the following slides as a minimum: Intro Page, transition slides, profile slides, slides for graphics,

```html
<!DOCTYPE html>
<html lang="en">
<head>
<meta charset="utf-8">
<title>Lanterfield Estate Partners – Presentation Template</title>
<link href="https://fonts.googleapis.com/css2?family=Montserrat:wght@800&family=Arimo:wght@400;700&display=swap" rel="stylesheet">
<style>
  :root {
    --board: #696969;
    --slide: #eeeeee;
    --ink: #222222;
    --ink-soft: #8f8f8f;
    --rule: #9a9a9a;
    --white: #ffffff;
    --band: #f2f2f2;
    --footer: #232323;
    --page-chip: #8a8274;
    --placeholder: #b9b9b9;
  }
  * { margin: 0; padding: 0; box-sizing: border-box; }
  html, body { width: 1200px; height: 907px; overflow: hidden; background: var(--board); }
  body { position: relative; font-family: "Arimo", Arial, sans-serif; }
  .slide { position: absolute; width: 582px; height: 436px; background: var(--slide); overflow: hidden; }
  .slide--brand { left: 14px; top: 10px; }
  .slide--cover { left: 605px; top: 10px; }
  .slide--content { left: 14px; top: 457px; }
  .slide--divider { left: 605px; top: 457px; }
  .abs { position: absolute; }
  .wordmark { font-family: "Montserrat", Arial, sans-serif; font-weight: 800; white-space: nowrap; letter-spacing: -0.3px; }

  /* brand slide */
  .brand-lockup { left: 0; right: 0; top: 202px; text-align: center; font-size: 26px; color: var(--ink); }

  /* cover slide */
  .cover-photo { left: 0; top: 0; width: 582px; height: 360px; }
  .cover-title { left: 14px; top: 14px; color: var(--white); font-family: "Montserrat", Arial, sans-serif; font-weight: 800; font-size: 31px; letter-spacing: -0.5px; line-height: 1; white-space: nowrap; }
  .cover-kicker { left: 14px; top: 51px; color: var(--white); font-size: 17px; white-space: nowrap; }
  .cover-audience { left: 16px; top: 93px; color: var(--ink-soft); font-size: 16px; line-height: 19px; white-space: nowrap; }
  .cover-audience b { color: #b5b5b5; }
  .cover-mark { right: 54px; top: 333px; font-size: 10px; color: var(--white); }
  .cover-band { left: 0; top: 360px; width: 582px; height: 76px; background: var(--band); }
  .cover-pointer { left: 444px; top: 360px; }
  .logo-slot { left: 15px; top: 374px; width: 49px; height: 49px; background: var(--placeholder); color: #888; font-size: 7px; text-align: center; padding-top: 36px; }
  .logo-slot svg { position: absolute; left: 14px; top: 10px; }
  .cover-deck-title { right: 18px; top: 388px; font-size: 22px; color: var(--ink); white-space: nowrap; }

  /* content slide */
  .slide-title { left: 12px; top: 4px; font-size: 22px; color: var(--ink-soft); white-space: nowrap; }
  .slide-subtitle { left: 13px; top: 28px; font-size: 13px; color: var(--ink-soft); white-space: nowrap; }
  .title-rule { left: 0; top: 45px; width: 436px; height: 1px; background: var(--rule); }
  .header-mark { right: 10px; top: 40px; font-size: 7.5px; color: var(--ink-soft); }
  .footer-bar { left: 0; top: 411px; width: 582px; height: 25px; background: var(--footer); color: var(--white); font-size: 11px; line-height: 25px; display: flex; align-items: center; white-space: nowrap; }
  .page-chip { width: 28px; height: 25px; background: var(--page-chip); text-align: center; flex: none; }
  .footer-mark { margin-left: 9px; font-size: 8px; line-height: 25px; }
  .footer-audience { margin-left: 10px; }

  /* divider slide */
  .divider-photo { left: 0; top: 0; }
  .divider-title { left: 101px; top: 187px; font-family: "Montserrat", Arial, sans-serif; font-weight: 800; font-size: 49px; color: var(--ink); letter-spacing: -0.5px; white-space: nowrap; }
  .divider-subtitle { left: 109px; top: 240px; font-size: 24px; color: var(--ink); white-space: nowrap; }
</style>
</head>
<body>

  <section class="slide slide--brand">
    <div class="abs brand-lockup wordmark">LANTERFIELD ESTATE PARTNERS</div>
  </section>

  <section class="slide slide--cover">
    <svg class="abs cover-photo" width="582" height="360" role="img" aria-label="Upward view of glass office towers and atrium roof">
      <defs>
        <linearGradient id="coverTone" x1="0" y1="0" x2="1" y2="1">
          <stop offset="0" stop-color="#3a3a3c"/>
          <stop offset="0.45" stop-color="#6c6e72"/>
          <stop offset="0.7" stop-color="#8d8f92"/>
          <stop offset="1" stop-color="#2d2d30"/>
        </linearGradient>
      </defs>
      <rect width="582" height="360" fill="url(#coverTone)"/>
    </svg>
    <div class="abs cover-title">LANTERFIELD</div>
    <div class="abs cover-kicker">COMPANY PRESENTATION</div>
    <div class="abs cover-audience">To <b>Business</b>/Corporation<br>JULY 2013</div>
    <div class="abs cover-mark wordmark">LANTERFIELD ESTATE PARTNERS</div>
    <div class="abs cover-band"></div>
    <svg class="abs cover-pointer" width="16" height="13"><polygon points="0,0 16,0 8,13" fill="#1e1e1e"/></svg>
    <div class="abs logo-slot">LOGO
      <svg width="21" height="19" viewBox="0 0 21 19"><rect x="1" y="1" width="19" height="17" fill="none" stroke="#8a8a8a" stroke-width="1.5"/><polygon points="3,16 9,8 13,13 15,11 18,16" fill="#8a8a8a"/><circle cx="15" cy="5.5" r="2" fill="#8a8a8a"/></svg>
    </div>
    <div class="abs cover-deck-title">COMPANY PRESENTATION TITLE</div>
  </section>

  <section class="slide slide--content">
    <div class="abs slide-title">SLIDE TITLE</div>
    <div class="abs slide-subtitle">Slide Subtitle</div>
    <div class="abs title-rule"></div>
    <div class="abs header-mark wordmark">LANTERFIELD ESTATE PARTNERS</div>
    <div class="abs footer-bar">
      <span class="page-chip">4</span>
      <span class="footer-mark wordmark">LANTERFIELD ESTATE PARTNERS</span>
      <span class="footer-audience">|&nbsp;&nbsp;To <b>Business</b>/Corporation</span>
    </div>
  </section>

  <section class="slide slide--divider">
    <svg class="abs divider-photo" width="582" height="436" role="img" aria-label="Angled strip of dark office tower facade">
      <defs>
        <linearGradient id="dividerTone" x1="0" y1="1" x2="1" y2="0">
          <stop offset="0" stop-color="#1f1f21"/>
          <stop offset="0.6" stop-color="#3b3c3f"/>
          <stop offset="1" stop-color="#7b7e82"/>
        </linearGradient>
      </defs>
      <polygon points="576,0 582,0 582,436 383,436" fill="url(#dividerTone)"/>
    </svg>
    <div class="abs divider-title">TRANSITION</div>
    <div class="abs divider-subtitle">Divider Slide Title</div>
  </section>

</body>
</html>
```